KelvaNest - Home Income and Business Resources Platform

I am looking for a website template for a multi-purposed website. This website will feature:

1.) Website Directory with Ratings & comments on listings
2.) Company Blog
3.) Homepage with Content (see files for homepage mock)

I would like the Design to have a default width 1170px (wider then normal)

Of course I am looking for Pages for Listings to be designed.

Great looking BLOG Layout: http://journal.pixelvorn.example/html/blog.html

I would like 4 Versions of a Website Directory Listing "Box"
1.) Basic Listing Box
2.) Sponsored Listing Box
3.) Recommended Listing Box
4.) Stay Away From Listing Box

Information on the Listing Page (Like on a Category Page)
Site Name, Site URL, Website Image, # of Views, Rating and # of Comments

Information on the Listing Details Page:
Same as ABOVE + About website Description, Trovix Rank, Category Information

Decent looking examples is here: https://demos.quendaro.example/directory/computers/ and http://www.zibrankhub.example/.

I will include some sketches and screenshots of things I like/looking for. As designers,you have creative freedom and are encouraged to show this. This is Phase one of this project and winning designer is guaranteed to have future work for this project.

Target Market(s)

Directory, business, websites

Industry/Entity Type

Business

Font styles to use
Sans Serif

Colors

Designer to choose colors to be used in the design.

Requirements
Must have
• Professional yet clean look. The use of Icons & images
• Unique Look
Should not have
• Any exact copies of any examples I provided

```html
<!DOCTYPE html>
<html lang="en">
<head>
<meta charset="utf-8">
<title>KelvaNest – Home Income and Business Resources</title>
<link href="https://fonts.googleapis.com/css2?family=Open+Sans:wght@400;600&family=Raleway:wght@200;300;400;500&display=swap" rel="stylesheet">
<style>
:root{
  --blue:#1565c8;
  --blue-soft:#2b78d6;
  --orange:#f76b0e;
  --ink:#333;
  --muted:#666;
  --line:#d6dde6;
  --panel:#f5f7fa;
  --card-border:#9fc1e8;
}
*{box-sizing:border-box;margin:0;padding:0}
html,body{width:674px;height:1200px;overflow:hidden;background:#fff}
body{position:relative;font-family:'Open Sans',sans-serif;color:var(--ink)}
.abs{position:absolute}

/* header */
.brand{left:52px;top:5px}
.brand-name{font-size:9.5px;font-weight:600;color:var(--blue);line-height:11px}
.brand-tag{font-size:4.5px;color:#333;line-height:6px}
.phone{right:52px;top:9px;font-size:7.5px;color:#555;display:flex;align-items:center;gap:3px}
.nav{left:52px;top:26px;width:570px;height:18px;background:var(--blue);display:flex;align-items:center;padding:0 8px}
.nav a{color:#fff;font-size:6.5px;font-weight:600;text-decoration:none;margin-right:9px;letter-spacing:.1px}
.nav .social{margin-left:auto;display:flex;gap:6px}
.nav .social span{width:6px;height:6px;background:#fff;display:block}

/* hero */
.hero{left:52px;top:53px;width:570px;height:190px;background:linear-gradient(120deg,#9fb4c0 0%,#c9d6dc 40%,#e9eef0 70%,#b9c4c6 100%);box-shadow:0 6px 10px -6px rgba(0,0,0,.35)}
.hero-badge{left:76px;top:74px;width:148px;height:148px;border-radius:50%;background:#fff;border:3px solid var(--blue-soft);display:flex;flex-direction:column;align-items:center;padding-top:30px;text-align:center}
.hero-badge h1{font-family:'Raleway',sans-serif;font-weight:400;font-size:10px;line-height:13px;color:var(--blue)}
.hero-badge hr{width:56px;border:0;border-top:1px solid #bbb;margin:5px 0 6px}
.hero-badge p{font-size:5.2px;line-height:7.5px;color:#555;width:112px}
.hero-badge .btn{margin-top:8px}

.btn{display:inline-flex;align-items:center;justify-content:center;width:79px;height:18px;background:var(--orange);color:#fff;font-size:6.5px;font-weight:600;text-decoration:none}
.btn.blue{background:var(--blue)}

/* feature cards */
.card{top:280px;width:114px;height:244px;border:1px solid var(--card-border);background:#fafcff;padding:9px 3px 0 6px}
.card svg{display:block;height:22px}
.card h2{font-family:'Raleway',sans-serif;font-weight:400;font-size:9px;line-height:12.5px;color:var(--blue);height:34px;margin-top:6px;display:flex;align-items:center;white-space:nowrap}
.card p{font-size:6.2px;line-height:10.9px;color:#555;margin-top:5px;height:132px;overflow:hidden}
.card .btn{position:absolute;left:5px;top:211px}

/* sidebar */
.sidebar{left:426px;top:277px;width:194px;height:887px;background:var(--panel)}
.avatar{left:61px;top:18px;width:74px;height:74px;border-radius:50%;background:radial-gradient(circle at 50% 40%,#d9a78a,#8a6a55 70%);border:3px solid #fff;box-shadow:0 0 0 1px #bbb}
.side-title{position:absolute;left:0;width:194px;text-align:center;font-family:'Raleway',sans-serif;font-weight:400;font-size:11px;color:var(--blue)}
.side-rule{position:absolute;left:0;width:194px;border-top:1px solid var(--line)}
.about-text{left:12px;top:116px;width:174px;font-size:6.4px;line-height:11.2px;color:#555}
.follow{left:0;top:277px;width:194px;display:flex;justify-content:center;gap:10px}
.follow span{width:16px;height:16px;background:var(--blue);position:relative}
.follow span::after{content:"";position:absolute;left:5px;bottom:-4px;border:3px solid transparent;border-top-color:var(--blue)}
.follow-label{left:0;top:297px;width:112px;text-align:right;font-size:5.5px;color:#333}
.recent-img{left:8px;width:178px;height:62px}
.recent-title{left:0;width:194px;text-align:center;font-size:6.6px;font-weight:600;color:#1e88d6}
.recent-date{left:0;width:194px;text-align:center;font-size:6.5px;color:#333}
.pager{top:574px;display:flex;gap:1px}
.pager span{width:12px;height:12px;background:var(--orange);display:flex;align-items:center;justify-content:center}
.promo{left:10px;top:633px;width:176px;height:244px;background:linear-gradient(180deg,#1d1d1d,#0a0a0a)}
.promo h3{position:absolute;left:8px;top:16px;font-family:'Raleway',sans-serif;font-weight:200;font-size:30px;line-height:43px;color:#fff}
.promo p{position:absolute;left:8px;top:102px;width:162px;font-size:6.5px;line-height:10.2px;color:#fff}

/* posts */
.post{left:54px;width:338px;height:180px}
.post-img{position:absolute;left:0;top:0;width:128px;height:180px}
.post-body{position:absolute;left:138px;top:0;width:202px}
.post h2{font-family:'Raleway',sans-serif;font-weight:400;font-size:11.5px;line-height:13px;color:#222;text-align:center;margin-top:14px;padding-left:16px}
.post .cats{text-align:center;padding-left:16px;font-size:5.8px;color:var(--blue);margin-top:8px;position:relative}
.post .cats::before{content:"";position:absolute;left:50%;margin-left:-4px;top:-4px;width:24px;border-top:1px solid #333}
.post .excerpt{font-size:6.2px;line-height:11.2px;color:#444;margin-top:8px}
.post .byline{font-size:6.4px;color:#333;margin-top:10px;padding-bottom:7px;border-bottom:1px solid var(--line)}
.post .byline b{font-weight:400;color:var(--blue);margin:0 3px}
.post .actions{display:flex;align-items:center;margin-top:6px}
.post .meta{margin-left:auto;display:flex;gap:8px;font-size:6px;color:#333;padding-right:4px}
.post .meta span{display:flex;align-items:center;gap:3px}

/* footer */
.footer-rule{left:0;top:1178px;width:674px;border-top:1px solid var(--blue-soft)}
.footer{left:52px;top:1186px;width:570px;display:flex;align-items:center;font-size:6px;color:#666}
.footer .dots{display:flex;gap:3px;margin-right:14px}
.footer .dots span{width:5px;height:5px;background:#666}
.footer a{color:#666;text-decoration:none;margin-right:7px}
.footer .copy{margin-left:auto}
</style>
</head>
<body>

<header>
  <div class="abs brand">
    <div class="brand-name">KelvaNest</div>
    <div class="brand-tag">Home Income and Business Resources</div>
  </div>
  <div class="abs phone">
    <svg width="7" height="7" viewBox="0 0 10 10"><path d="M2 0.5l2 2-1 1.3c.6 1.3 1.6 2.3 2.9 2.9l1.3-1 2 2-1.2 1.7C4.6 9.2.8 5.4.3 1.7z" fill="#1565c8"/></svg>
    0800-000-000-000
  </div>
  <nav class="abs nav">
    <a href="#">HOME</a><a href="#">ABOUT</a><a href="#">PAGE TEMPLATES</a><a href="#">SHORTCODES</a><a href="#">SHOP PAGE</a><a href="#">CONTACT</a>
    <div class="social"><span></span><span></span><span></span></div>
  </nav>
</header>

<section class="abs hero" role="img" aria-label="Photo of hands working at a laptop with paperwork and a pen"></section>
<div class="abs hero-badge">
  <h1>Home Income<br>and Business Resources</h1>
  <hr>
  <p>Lorem Ipsum is simply dummy text of the printing and typesettin Lorem Ipsum has been the industry's standard dummy text</p>
  <a class="btn" href="#">Read More</a>
</div>

<section>
  <article class="abs card" style="left:52px">
    <svg viewBox="0 0 28 22" width="28"><circle cx="17" cy="7" r="5" fill="none" stroke="#222" stroke-width="1.4"/><path d="M2 15h6l5 3h8l5-4" fill="none" stroke="#222" stroke-width="1.4"/><path d="M2 12h6v8H2z" fill="var(--orange)"/></svg>
    <h2>Home Income<br>Resource Directory</h2>
    <p>Text: Find what you need, when you need it.The KelvaNest website directory is your one-stop pit for anything involved in making money from home, marketing your business or finding a new opportunity. Our modern, community supported directory will help you keep upto todate with the lastest information in a sensibl</p>
    <a class="btn" href="#">Read More</a>
  </article>
  <article class="abs card" style="left:176px">
    <svg viewBox="0 0 28 22" width="28"><rect x="4" y="2" width="20" height="13" fill="none" stroke="#222" stroke-width="1.4"/><path d="M8 12V9M12 12V6M16 12V8M20 12V4" stroke="var(--orange)" stroke-width="1.6"/><path d="M14 15v4M9 21l5-2 5 2" stroke="#222" stroke-width="1.4" fill="none"/></svg>
    <h2>Advertising Benefits</h2>
    <p>Text: Everyone needs to advertise and we know just how to get your offer out to the right people. We have many methods including: Text ads, E-mail, Display, newsletter and even some old school methods available to make your next campaign a success. Advertise a website, a link text, full page circular or a small display ad and get</p>
    <a class="btn blue" href="#">Read More</a>
  </article>
  <article class="abs card" style="left:300px">
    <svg viewBox="0 0 28 22" width="28"><circle cx="17" cy="7" r="5" fill="none" stroke="#222" stroke-width="1.4"/><path d="M2 15h6l5 3h8l5-4" fill="none" stroke="#222" stroke-width="1.4"/><path d="M2 12h6v8H2z" fill="var(--orange)"/></svg>
    <h2>Earning With KelvaNest</h2>
    <p>Text: Join KelvaNest and start earning money. When you share KelvaNest and lock in an advertiser or premium listing, we reward you. Build a downline at any of our listed sites when you share KelvaNest with NO extra work. Its all done for you.We also offer a revenue share program for true supporters of our mission.</p>
    <a class="btn" href="#">Read More</a>
  </article>
</section>

<aside class="abs sidebar">
  <div class="abs avatar" role="img" aria-label="Portrait photo of a team member"></div>
  <h3 class="side-title" style="top:98px">About Us</h3>
  <p class="abs about-text">Lorem Ipsum is simply dummy text of the printing and typesetting industry. Lorem Ipsum has been the industry's standard dummy text ever since the 1500s, when an wn printer took a galley of type and scrambled it to make a type specimen book. Lorem Ipsum is simply dummy text of the printing and type-setting industry. Lorem Ipsum has been the indus-try's standard dummy text ever since the 1500s, when an unknown printer took a galley of type and</p>

  <h3 class="side-title" style="top:237px">Social Media</h3>
  <div class="side-rule" style="top:256px"></div>
  <div class="abs follow"><span></span><span></span><span></span><span></span><span></span></div>
  <div class="abs follow-label">Follow Us</div>

  <h3 class="side-title" style="top:327px">Recent Posts</h3>
  <div class="side-rule" style="top:345px"></div>
  <div class="abs recent-img" style="top:359px;background:linear-gradient(100deg,#a88a5c,#6f8a3c 45%,#c9a27c)" role="img" aria-label="Photo of a woman blowing bubbles outdoors"></div>
  <div class="abs recent-title" style="top:426px">Regular Exercise is a Natural Anti-Inflammatory</div>
  <div class="abs recent-date" style="top:441px">August 22, 2016</div>
  <div class="abs recent-img" style="top:465px;background:linear-gradient(180deg,#8fb0c8,#5c6f6a 45%,#6d7a3f 80%,#b3485a)" role="img" aria-label="Photo of a stone cottage with flowers in the mountains"></div>
  <div class="abs recent-title" style="top:532px">Regular Exercise is a Natural Anti-Inflammatory</div>
  <div class="abs recent-date" style="top:547px">August 22, 2016</div>
  <div class="abs pager" style="left:84px">
    <span><svg width="5" height="7" viewBox="0 0 5 7"><path d="M4 0.5L1 3.5 4 6.5" stroke="#fff" fill="none"/></svg></span>
    <span><svg width="5" height="7" viewBox="0 0 5 7"><path d="M1 0.5L4 3.5 1 6.5" stroke="#fff" fill="none"/></svg></span>
  </div>

  <h3 class="side-title" style="top:600px">Hey Warriors, We Support You!</h3>
  <div class="side-rule" style="top:620px"></div>
  <div class="abs promo">
    <h3>Advertising<br>Benefits</h3>
    <p>Action plan chronic chronic illness chronic illness pain chronic pain coping with a chronic illness depression employment energy failure fibro fibro-myalgia focus food diary functional medicine goal action plan goals inflammation invisible illness job job hunting life goals live with chronic illness living with long term condition long term condition manage chronic pain meditation natural remedies pain pain control parenting with chronic illness passion quit job resolutions self awareness setback side hustle side hustling SMART goals spoon theory success yoga</p>
  </div>
</aside>

<main>
  <article class="abs post" style="top:550px">
    <div class="post-img" style="background:linear-gradient(160deg,#6c8a4a,#c8b2a6 55%,#d8c6c0)" role="img" aria-label="Photo of a smiling woman talking on a phone"></div>
    <div class="post-body">
      <h2>Chronic Illness and Starting an Exercise Regimen</h2>
      <div class="cats">Daily Living, Health</div>
      <p class="excerpt">Your general health is intimately connected with the foods and drinks you put into your body. Each person is unique in what food or drink can trigger feeling unhealthy and rundown. It is very easy to lose track of which foods and drinks can be wreaking havoc with your health. A great way to do some detective work</p>
      <div class="byline">Written by<b>Mara Lindqvist</b>in<b>August 22, 2016</b></div>
      <div class="actions"><a class="btn" href="#">Read More</a>
        <div class="meta">
          <span><svg width="7" height="6" viewBox="0 0 7 6"><ellipse cx="3.5" cy="2.6" rx="3.5" ry="2.6" fill="var(--blue-soft)"/><path d="M1 4l-1 2 3-1z" fill="var(--blue-soft)"/></svg>05</span>
          <span><svg width="7" height="6" viewBox="0 0 7 6"><path d="M3.5 6L0.4 2.8A1.7 1.7 0 013.5 .8a1.7 1.7 0 013.1 2z" fill="var(--blue-soft)"/></svg>02</span>
        </div>
      </div>
    </div>
  </article>

  <article class="abs post" style="top:755px">
    <div class="post-img" style="background:linear-gradient(150deg,#6a4a34,#9b6f4c 40%,#2c3a5a 75%,#1c2440)" role="img" aria-label="Photo of a laptop and a key fob on a wooden desk"></div>
    <div class="post-body">
      <h2>Chronic Illness and Starting an Exercise Regimen</h2>
      <div class="cats">Daily Living, Health</div>
      <p class="excerpt">Your general health is intimately connected with the foods and drinks you put into your body. Each person is unique in what food or drink can trigger feeling unhealthy and rundown. It is very easy to lose track of which foods and drinks can be wreaking havoc with your health. A great way to do some detective work</p>
      <div class="byline">Written by<b>Mara Lindqvist</b>in<b>August 22, 2016</b></div>
      <div class="actions"><a class="btn blue" href="#">Read More</a>
        <div class="meta">
          <span><svg width="7" height="6" viewBox="0 0 7 6"><ellipse cx="3.5" cy="2.6" rx="3.5" ry="2.6" fill="var(--blue-soft)"/><path d="M1 4l-1 2 3-1z" fill="var(--blue-soft)"/></svg>05</span>
          <span><svg width="7" height="6" viewBox="0 0 7 6"><path d="M3.5 6L0.4 2.8A1.7 1.7 0 013.5 .8a1.7 1.7 0 013.1 2z" fill="var(--blue-soft)"/></svg>02</span>
        </div>
      </div>
    </div>
  </article>

  <article class="abs post" style="top:958px">
    <div class="post-img" style="background:linear-gradient(160deg,#8a6a4e,#d7d9dc 45%,#b8c6d4 80%,#e6e2da)" role="img" aria-label="Photo of hands typing on a laptop beside a coffee cup"></div>
    <div class="post-body">
      <h2>Chronic Illness and Starting an Exercise Regimen</h2>
      <div class="cats">Daily Living, Health</div>
      <p class="excerpt">Your general health is intimately connected with the foods and drinks you put into your body. Each person is unique in what food or drink can trigger feeling unhealthy and rundown. It is very easy to lose track of which foods and drinks can be wreaking havoc with your health. A great way to do some detective work</p>
      <div class="byline">Written by<b>Mara Lindqvist</b>in<b>August 22, 2016</b></div>
      <div class="actions"><a class="btn" href="#">Read More</a>
        <div class="meta">
          <span><svg width="7" height="6" viewBox="0 0 7 6"><ellipse cx="3.5" cy="2.6" rx="3.5" ry="2.6" fill="var(--blue-soft)"/><path d="M1 4l-1 2 3-1z" fill="var(--blue-soft)"/></svg>05</span>
          <span><svg width="7" height="6" viewBox="0 0 7 6"><path d="M3.5 6L0.4 2.8A1.7 1.7 0 013.5 .8a1.7 1.7 0 013.1 2z" fill="var(--blue-soft)"/></svg>02</span>
        </div>
      </div>
    </div>
  </article>
</main>

<div class="abs footer-rule"></div>
<footer class="abs footer">
  <div class="dots"><span></span><span></span><span></span></div>
  <a href="#">About Us</a><a href="#">Privacy Policy</a><a href="#">Terms of Use</a><a href="#">Advertise Us</a><a href="#">Help</a>
  <span class="copy">© 2017 Copyright</span>
</footer>

</body>
</html>
```